Kestrel Brewery bottle label design Vietnam

This is a label design for Kestrel Brewery locate in Saigon city,Vietnam. A label for 330ml brown beer bottle.
The company has its logo and now it needs designer to help it develops the label for its first Riverlight Pale Ale 5.3% alcohol. The other type of beer just change the name and color to follow the design concept.
Kestrel Brewery is inspired by sunny city, its location and what belong to Saigon city like Saigon river, Saigon city post office, Orvane 47 buiding,Dravilo building, but not limit to these only.You can be creative to other thing to Saigon city.
The design can reflect Riverlight people characters like open to new things, new ideas ,just like craft beer is very creative.
I am waiting for your reply
Thanks.

Target Market(s)

Young men women 20 to 50 years old who know craft beer and middle class consumers

Font styles to use
Decorative

Requirements
Must have
• sunny and reflect Saigon city
Nice to have
• Hops.Malt

```html
<!DOCTYPE html>
<html lang="en">
<head>
<meta charset="utf-8">
<title>Kestrel Brewery – Riverlight Pale Ale Label</title>
<link rel="stylesheet" href="https://fonts.googleapis.com/css2?family=Great+Vibes&family=Montserrat:wght@500;700&family=Tinos:wght@400;700&display=swap">
<style>
  :root {
    --backdrop: #cfcfcf;
    --label-black: #1c1b1b;
    --pattern-black: #242323;
    --ring-grey: #3a3939;
    --cream: #f1ead9;
    --orange: #f0901e;
    --orange-light: #f5b25a;
    --ink: #1a1512;
    --spec-brown: #7a4a16;
  }
  * { margin: 0; padding: 0; box-sizing: border-box; }
  html, body { width: 1011px; height: 1200px; overflow: hidden; }
  body { background: var(--backdrop); position: relative; }

  .label { position: absolute; left: 205px; top: 100px; width: 600px; height: 1000px; }
  .label-art { position: absolute; inset: 0; }

  .brand-name {
    position: absolute; left: 200px; top: 150px; width: 200px;
    text-align: center; color: var(--cream);
    font: 700 22px/1.15 "Montserrat", sans-serif; letter-spacing: 1px; text-transform: uppercase;
  }

  .beer-name {
    position: absolute; left: 0; right: 0; top: 360px; text-align: center;
    color: var(--cream); font: 400 92px/1 "Great Vibes", cursive;
  }
  .beer-style {
    position: absolute; left: 345px; top: 464px;
    color: var(--cream); font: 500 28px/1 "Montserrat", sans-serif; letter-spacing: 2px;
  }
  .tagline {
    position: absolute; left: 0; right: 0; top: 526px; text-align: center;
    color: var(--cream); font: 700 21px/28px "Tinos", serif; text-transform: uppercase; letter-spacing: .5px;
  }
  .quality {
    position: absolute; left: 0; right: 0; top: 782px; text-align: center;
    color: var(--ink); font: 400 46px/1 "Great Vibes", cursive;
  }
  .quality::before, .quality::after {
    content: ""; display: inline-block; width: 22px; height: 3px; background: var(--ink);
    vertical-align: middle; margin: 0 10px;
  }
  .spec {
    position: absolute; top: 852px; width: 60px; text-align: center;
    color: var(--spec-brown); font: 400 18px/20px "Tinos", serif;
  }
  .spec--abv { left: 42px; }
  .spec--volume { right: 42px; }
</style>
</head>
<body>
  <div class="label">
    <svg class="label-art" width="600" height="1000" viewBox="0 0 600 1000" xmlns="http://www.w3.org/2000/svg">
      <defs>
        <linearGradient id="orange-band" x1="0" y1="0" x2="0" y2="1">
          <stop offset="0" stop-color="#f5b25a"/>
          <stop offset="1" stop-color="#f0901e"/>
        </linearGradient>
        <linearGradient id="skyline-fade" x1="0" y1="0" x2="0" y2="1">
          <stop offset="0" stop-color="#2a2220"/>
          <stop offset="1" stop-color="#f5b25a"/>
        </linearGradient>
      </defs>

      <rect class="label-body" x="0" y="200" width="600" height="420" fill="var(--label-black)"/>
      <rect x="10" y="215" width="580" height="395" fill="var(--pattern-black)" role="img" aria-label="Dark damask ornament pattern"/>
      <rect x="0" y="610" width="600" height="170" fill="url(#skyline-fade)" role="img" aria-label="Saigon skyline silhouette with Orvane 47, Dravilo tower and the city post office"/>
      <rect class="orange-band" x="0" y="780" width="600" height="220" fill="url(#orange-band)"/>

      <rect class="inner-frame" x="20" y="206" width="560" height="740" fill="none" stroke="var(--cream)" stroke-width="2"/>
      <rect x="26" y="212" width="548" height="728" fill="none" stroke="var(--cream)" stroke-width="1" opacity=".6"/>

      <circle class="badge" cx="300" cy="179" r="166" fill="var(--label-black)"/>
      <circle cx="300" cy="179" r="150" fill="var(--ring-grey)" role="img" aria-label="Ring of hop cones"/>
      <circle cx="300" cy="179" r="108" fill="var(--label-black)" stroke="var(--cream)" stroke-width="3"/>
    </svg>

    <div class="brand-name">Kestrel Brewery</div>

    <div class="beer-name">Riverlight</div>
    <div class="beer-style">PALE ALE</div>
    <p class="tagline">A beer can tell a story<br>and represents its city<br>product of Vietnam</p>

    <div class="quality">Premier Quality</div>
    <div class="spec spec--abv">~<br>5.3<br>ALC<br>~</div>
    <div class="spec spec--volume">~<br>330<br>ML<br>~</div>
  </div>
</body>
</html>
```